Pepper Meadow Indian Restaurant - Easter Dinner Buffet

Pepper Meadow is an Indian restaurant located in Perth's northern suburbs. We are offering a Special Easter Dinner buffet which runs during all public holidays.

The key points is
1. 35+ Items on the menu
2. Sea Food ,Goat , Lamb, Chicken Varieties
3. Plenty of options for Vegetarians and Vegans,
4. Available during all Easter Holidays (5:30PM-9:30PM)
5. Only available for Dine In
6. Adult Price $34.50; Kids under 12 eat at $21. Kids under 2 Free

Items on the menu are as below.

S.No Category Item
1 Soup Lentil Soup
2 Veg Starters Saudi Aloo (Potato)
3 Veg Starters Veg Pakora
4 Veg Starters Onion Bhaji
5 Veg Starters Veg Samosa
6 Veg Starters Potato Pakora
7 Veg Starters Chutney Aloo (Potato)
8 NV Starters Tandoori Chicken
9 NV Starters Murg (Chicken) Kali Tikka
10 NV Starters Chicken 65
11 NV Starters Lemon Chicken Tikka
12 Veg Curries Potato Curry
13 Veg Curries Mix Vegetable Curry
14 Veg Curries Mushrool Masala
15 Veg Curries Yellow Dal
16 NV Curries Fish Fry
17 NV Curries Goat Curry
18 NV Curries Butter Chicken
19 NV Curries Lamb Rogan Josh
20 NV Curries Goan Fish Curry
21 NV Curries Special Chicken Curry
22 Rice Prawn Biryani
23 Rice Steamed Rice
24 Rice Saffron Rice
25 Breads Chocolate Naan
26 Breads Butter Naan
27 Breads Garlic Nann
28 Sides Raitha
29 Sides Papadam
30 Sides Salad
31 Dessert Gulab Jamun
32 Dessert Fruit Custard
33 Dessert Semiya Payasam
34 Dessert Coconut Pudding

Industry/Entity Type

Restaurant

Requirements
Must have
• Title
• Easter Buffet - Extravagant Family Buffet

```html
<!DOCTYPE html>
<html lang="en">
<head>
<meta charset="utf-8">
<title>Special Easter Buffet Menu</title>
<link rel="stylesheet" href="https://fonts.googleapis.com/css2?family=Cinzel:wght@400;700&family=Great+Vibes&family=Raleway:wght@400;700&display=swap">
<style>
  :root {
    --paper: #f5f3ef;
    --paper-warm: #f7ecd6;
    --band-left: #f1dcae;
    --band-right: #f3d9a6;
    --side-stripe: #e6e6ea;
    --title-pink: #c7465c;
    --ink: #2f2f35;
    --ink-blue: #3c5f8f;
    --heading-blue: #4a72a6;
    --heading-green: #2a9a34;
    --heading-red: #d2222c;
    --divider: #5b7fb0;
    --price-gold: #cdbb5e;
    --price-tan: #c6ab86;
    --price-blue: #6f8fb8;
    --grass: #6cbf3a;
    --grass-dark: #3f9a22;
    --egg-grey: #9a9a9a;
    --egg-red: #e2665a;
    --flower-grey: #8a8f8c;
  }
  * { box-sizing: border-box; margin: 0; padding: 0; }
  html, body { width: 880px; height: 1200px; overflow: hidden; }
  body { background: #e9e9e9; font-family: "Raleway", sans-serif; }

  .poster {
    position: relative; width: 880px; height: 1200px; overflow: hidden;
    background: linear-gradient(90deg, var(--band-left) 0%, var(--paper) 8%, var(--paper) 50%, var(--paper-warm) 80%, var(--band-right) 100%);
  }
  .side-stripe { position: absolute; top: 0; bottom: 0; width: 44px; background: linear-gradient(180deg, rgba(230,230,236,.8), rgba(240,236,226,.4)); }
  .side-stripe.left { left: 52px; }
  .side-stripe.right { right: 52px; }

  .art { position: absolute; }
  .wreath { left: 140px; top: 0; width: 600px; height: 300px; border-radius: 0 0 300px 300px;
    background: radial-gradient(ellipse at 50% 40%, rgba(138,143,140,.35), rgba(180,160,120,.15) 70%, transparent 72%); }
  .egg { width: 58px; height: 80px; border-radius: 50% 50% 48% 48% / 60% 60% 40% 40%; background: linear-gradient(180deg, #b8b8b8, var(--egg-grey)); opacity: .8; }
  .egg.red { background: linear-gradient(180deg, #f08a7a, var(--egg-red)); }
  .bunny-left { left: 345px; top: 1100px; width: 300px; height: 70px; background: linear-gradient(180deg, rgba(235,235,235,.9), rgba(240,190,200,.6)); border-radius: 40px 40px 0 0; }
  .bunny-right { left: 690px; top: 1030px; width: 150px; height: 170px; background: linear-gradient(180deg, #f4f1ec, #ffffff); border-radius: 70px 70px 0 0; }
  .grass { left: 0; top: 1128px; width: 880px; height: 72px; background: linear-gradient(180deg, var(--grass), var(--grass-dark)); }

  .header-disc { position: absolute; left: 202px; top: -123px; width: 470px; height: 470px; border-radius: 50%; background: #fff; box-shadow: 0 0 0 6px rgba(255,255,255,.6); }
  .header-mark { position: absolute; left: 413px; top: 40px; width: 70px; height: 26px; border-radius: 13px; background: #f08c9a; }

  .centered { position: absolute; left: 0; width: 880px; text-align: center; font-family: "Cinzel", serif; }
  .kicker { top: 78px; font-size: 24px; letter-spacing: 9px; color: var(--ink); }
  .title { top: 102px; font-size: 44px; color: var(--title-pink); letter-spacing: 1px; }
  .subtitle { top: 158px; font-size: 21px; line-height: 26px; color: var(--ink); letter-spacing: 1px; }

  .highlight { font-size: 15px; color: var(--ink-blue); }
  .h-items { top: 305px; }
  .h-varieties { top: 328px; font-size: 20px; font-weight: 700; }
  .h-veg { top: 358px; color: var(--ink); }
  .h-hours { top: 382px; }
  .h-dinein { top: 407px; }

  .price { position: absolute; top: 436px; height: 46px; width: 206px; border-radius: 8px; color: #fff; font-family: "Cinzel", serif; font-size: 17px; line-height: 18px; display: flex; align-items: center; justify-content: center; text-align: center; }
  .price.adult { left: 118px; background: var(--price-gold); }
  .price.kids { left: 337px; background: var(--price-tan); }
  .price.infant { left: 555px; background: var(--price-blue); }

  .menu-title { position: absolute; top: 505px; left: 0; width: 880px; text-align: center; font-family: "Great Vibes", cursive; font-size: 84px; color: var(--heading-blue); }

  .divider { position: absolute; top: 638px; width: 2px; height: 388px; background: var(--divider); }
  .column { position: absolute; top: 632px; }
  .col-a { left: 125px; } .col-b { left: 376px; } .col-c { left: 606px; }
  .course h2 { font-size: 16px; font-weight: 700; margin-bottom: 10px; }
  .course ul { list-style: none; font-size: 16px; line-height: 21.6px; color: var(--ink); }
  .blue h2 { color: var(--heading-blue); }
  .green h2 { color: var(--heading-green); }
  .red h2 { color: var(--heading-red); }
  .gap-lg { margin-top: 33px; }
  .gap-sm { margin-top: 12px; }
  .gap-md { margin-top: 18px; }
</style>
</head>
<body>
<main class="poster">
  <div class="side-stripe left"></div>
  <div class="side-stripe right"></div>

  <div class="art wreath" role="img" aria-label="Wreath of roses and leaves framing the header"></div>
  <div class="art egg" style="left:0;top:140px" role="img" aria-label="Hanging decorated Easter egg"></div>
  <div class="art egg" style="left:103px;top:270px" role="img" aria-label="Hanging decorated Easter egg"></div>
  <div class="art egg" style="left:700px;top:270px" role="img" aria-label="Hanging decorated Easter egg"></div>
  <div class="art egg red" style="left:820px;top:100px" role="img" aria-label="Hanging red decorated Easter egg"></div>

  <div class="header-disc"></div>
  <div class="header-mark" role="img" aria-label="Pair of pink patterned Easter eggs"></div>

  <p class="centered kicker">Special</p>
  <h1 class="centered title">Easter Buffet</h1>
  <p class="centered subtitle">Extravagant Family<br>Buffet</p>

  <p class="centered highlight h-items">35+Items on the Menu</p>
  <p class="centered highlight h-varieties">Sea Food, Goat, Lamb, Chicken Varieties</p>
  <p class="centered highlight h-veg">Plenty of options for Vegetarians and Vegans</p>
  <p class="centered highlight h-hours">Available during all Easter Holidays (5:30PM-9:30PM)</p>
  <p class="centered highlight h-dinein">Only available for Dine In</p>

  <div class="price adult">Adult Price $34.50</div>
  <div class="price kids">Kids under 12 eat<br>at $21</div>
  <div class="price infant">Kids under 2 Free</div>

  <h2 class="menu-title">Menu</h2>

  <div class="divider" style="left:353px"></div>
  <div class="divider" style="left:583px"></div>

  <section class="column col-a">
    <div class="course blue"><h2>SOUP</h2><ul><li>Lentil Soup</li></ul></div>
    <div class="course green gap-lg"><h2>VEG STARTERS</h2><ul>
      <li>Saudi Aloo (Potato)</li><li>Veg Pakora</li><li>Onion Bhaji</li><li>Veg Samosa</li><li>Potato Pakora</li><li>Chutney Aloo (Potato)</li></ul></div>
    <div class="course green gap-lg"><h2>NV STARTERS</h2><ul>
      <li>Tandoori Chicken</li><li>Murg (Chicken) Kali Tikka</li><li>Chicken 65</li><li>Lemon Chicken Tikka</li></ul></div>
  </section>

  <section class="column col-b">
    <div class="course green"><h2>VEG CURRIES</h2><ul>
      <li>Potato Curry</li><li>Mix Vegetable Curry</li><li>Mushrool Masala</li><li>Yellow Dal</li></ul></div>
    <div class="course red gap-sm"><h2>NV CURRIES</h2><ul>
      <li>Fish Fry</li><li>Goat Curry</li><li>Butter Chicken</li><li>Lamb Rogan Josh</li><li>Goan Fish Curry</li><li>Special Chicken Curry</li></ul></div>
    <div class="course blue gap-sm"><h2>RICE</h2><ul>
      <li>Prawn Biryani</li><li>Steamed Rice</li><li>Saffron Rice</li></ul></div>
  </section>

  <section class="column col-c">
    <div class="course blue"><h2>BREADS</h2><ul>
      <li>Chocolate Naan</li><li>Butter Naan</li><li>Garlic Nann</li></ul></div>
    <div class="course blue gap-md"><h2>SIDES</h2><ul>
      <li>Raitha</li><li>Papadam</li><li>Salad</li></ul></div>
    <div class="course blue gap-md"><h2>DESSERT</h2><ul>
      <li>Gulab Jamun</li><li>Fruit Custard</li><li>Semiya Payasam</li><li>Coconut Pudding</li></ul></div>
  </section>

  <div class="art grass" role="img" aria-label="Strip of green grass along the bottom"></div>
  <div class="art bunny-left" role="img" aria-label="Bunny ears peeking out of the grass"></div>
  <div class="art bunny-right" role="img" aria-label="White Easter bunny peeking up in the corner"></div>
</main>
</body>
</html>
```